Online Psychiatry business - Business Card

I need a business card design. The target audience is busy professionals of any field (this therapy appeals best to 24-35 year olds). It involves psychiatry by tele-medicine (or video-conference). Nothing on it should be a giveaway that it's about mental health. Professional design with silver or gold as the primary colors appeals to me. The card must be as simple and as uncluttered as possible. Some color and flowing design on the edge of the card appeals to me.
CrestMindLink.com should probably appear in the center of the card and stand out, i.e. bold lettering, and easy to read, no cursive, but Ariel Black. Some where below this, should appear "Too Busy to Take Care of Yourself? Think again." Since this isn't office based, I don't think an office address is necessary and limits clutter.
Information that does need to appear is my name: Gerald Whitcombe, MD
General phone number: 541-876-2209. I'm hoping to get an 24-hour answering service soon so leave a little room for this. In addition I want to include two email addresses:
CrestMindLink@maildrop-box.com and CrestMind247@maildrop-box.com
Updates

I like the designs. I would like someone to put the website in bold in the center

 as most have been doing with a smaller font reminder nearby saying "No time" etc.
but I'd like to put my name down in the corner with the rest of the contact material.
Black print against a white or grey background appeals to me, with darker silver artwork near the sides (simple abstract, like wavy lines or something you can one up with that works. 
thanks

I ve tried to provide as much feedback as possible given my time limits, so if you have extra questions, please feel free to email. I tried to attach a file of a business card I really like but make be difficult to actually manufacture. I'm going to send you a link to the photo. The card has a pull tab. There is not much information on the outside. In fact, if you were to design the outside, I would just print : Too Busy to Take Care of Yourself? Think Again.

When you pull the tab the remaining information is on the bottom half of the card. Please don't use the color pink!!!!
http://www.layoutgallerypost.com/2009/05/100-clever-card-ideas/
It is the 39th photo on the list, about 2/3ds of the way down the page. It is titled: Faltenkästli

#7 and #16 have an appeal to me, except for the dot patterns
Hope this helps

I'm running out of time and energy. I 've been trying to give do down the list and give  individual feedback but I won't be able to do that anymore.

So if you have any specific questions, write me, and again thank you for all your effort!!

I know i received your files, including your zip files, Plonix,

but Gideon, did you send me the files including ZIP on project 5914386?
thanks

Target Market(s)

Working professionals and executive, attorneys, etc.

Industry/Entity Type

Business

Logo Text

Don't Have Time to Take Care of Yourself? Think Again.

Logo styles of interest
Pictorial/Combination Logo
Wordmark Logo
Other font styles liked:
• Ariel Black appeals to me the most

Requirements
Must have
• Want to emphasize that the website must be obvious, easily found (The CrestMindLink.com)
For that reason i'd like the card to be white, and minimal decoration on one or both sides just to add some style and color
Nice to have
• A Very uncluttered, elegant design, and something that makes it stick in your head-doesn't everyone want the last?
Should not have
• Nothing on the card that give it away that this is about psychiatry, such as brain or other symbol, but also nothing that gives it away as a medical business, such as a stethoscope or red cross or anything.

```html
<!DOCTYPE html>
<html lang="en">
<head>
<meta charset="utf-8">
<title>CrestMindLink.com – Business Card</title>
<link href="https://fonts.googleapis.com/css2?family=Mulish:wght@400;700;800&family=Questrial&display=swap" rel="stylesheet">
<style>
  :root {
    --page-bg: #e9e9e7;
    --card-white: #ffffff;
    --card-grey: #5d5d5d;
    --ink: #4a4a4a;
    --ink-soft: #5a5a5a;
    --band-dark: #6a6a6a;
    --band-light: #d6d6d6;
    --quote-ink: #ffffff;
  }
  * { margin: 0; padding: 0; box-sizing: border-box; }
  html, body {
    width: 1200px;
    height: 1000px;
    overflow: hidden;
    background: var(--page-bg);
  }
  .canvas {
    position: relative;
    width: 1200px;
    height: 1000px;
  }
  .card {
    position: absolute;
    left: 210px;
    width: 780px;
    height: 440px;
    border-radius: 38px;
    overflow: hidden;
    box-shadow: 0 6px 18px rgba(0,0,0,0.18);
  }
  .card--front { top: 45px; background: var(--card-white); }
  .card--back  { top: 515px; background: var(--card-grey); }

  .wave {
    position: absolute;
    inset: 0;
    width: 100%;
    height: 100%;
  }
  .wave__light { fill: var(--band-light); }
  .wave__dark  { fill: var(--band-dark); }

  .website {
    position: absolute;
    left: 0; right: 0;
    top: 140px;
    text-align: center;
    font-family: "Mulish", sans-serif;
    font-weight: 800;
    font-size: 44px;
    letter-spacing: -0.5px;
    color: var(--ink);
  }
  .phone {
    position: absolute;
    right: 34px;
    top: 330px;
    display: flex;
    align-items: center;
    gap: 8px;
    font-family: "Mulish", sans-serif;
    font-size: 19px;
    color: var(--ink-soft);
  }
  .phone__icon { width: 16px; height: 18px; fill: var(--ink-soft); }
  .name {
    position: absolute;
    left: 36px;
    bottom: 22px;
    font-family: "Mulish", sans-serif;
    font-size: 22px;
    color: var(--ink);
  }
  .name__person { font-weight: 700; }
  .name__title { font-weight: 400; color: var(--ink-soft); }

  .tagline {
    position: absolute;
    left: 0; right: 0;
    top: 148px;
    text-align: center;
    font-family: "Questrial", sans-serif;
    font-size: 35px;
    line-height: 1.25;
    color: var(--quote-ink);
  }
</style>
</head>
<body>
<main class="canvas">
  <section class="card card--front" aria-label="Business card front">
    <svg class="wave" viewBox="0 0 780 440" preserveAspectRatio="none" aria-hidden="true">
      <path class="wave__light" d="M0,280 C120,272 170,335 260,332 C420,328 600,245 780,205 L780,219 C600,259 420,342 260,346 C170,349 120,286 0,294 Z"/>
      <path class="wave__dark" d="M0,300 C120,292 170,355 260,352 C420,348 600,265 780,225 L780,251 C600,291 420,374 260,378 C170,381 120,318 0,326 Z"/>
    </svg>
    <h1 class="website">CrestMindLink.com</h1>
    <p class="phone">541-876-2209
      <svg class="phone__icon" viewBox="0 0 16 18" aria-hidden="true">
        <path d="M4,1 C2,2 1,4 1,7 C1,11 4,16 8,17 C10,17.5 12,17 13,15.5 L10.5,12.5 C9.5,13.2 8.6,13.2 8,12.5 C6.5,11 5.5,8.5 5.8,6.8 C6,6 6.8,5.6 7.5,5.5 L6.5,1 Z"/>
      </svg>
    </p>
    <p class="name"><span class="name__person">Gerald Whitcombe</span><span class="name__title">, MD</span></p>
  </section>

  <section class="card card--back" aria-label="Business card back">
    <p class="tagline">"Too Busy to Take Care of Yourself?<br>Think again."</p>
  </section>
</main>
</body>
</html>
```